Banner Ad Design Project

My online radio station features DJ sets periodically. The series is called "Deep Orbit" I need a versatile banner ad that I can add the DJ image to an area and then the date and time. I would assume we would agree the area where I can just add a layer via Photoshop with the DJ image and time info as I have more DJs. I will add one of my DJs images. You can crop as necessary. His airplay time is Friday 2pm set and 8pm set.

This is a DANCE radio station, so bright lights, lasers, etc will all be considered.

The banner size is 960X340

Target Market(s)

LGBT between 16-45

Industry/Entity Type

Radio

Requirements
Should not have
• although this is for LGBT, I do not want to see rainbow flags, headphones or other cheesy common themes

```html
<!DOCTYPE html>
<html lang="en">
<head>
<meta charset="utf-8">
<title>Deep Orbit – DJ Set Banner</title>
<link rel="stylesheet" href="https://fonts.googleapis.com/css2?family=Oswald:wght@500&family=Oxanium:wght@600&family=Share+Tech+Mono&family=Tinos&family=Arimo&display=swap">
<style>
  :root{
    --stage-light:#5c5c5c;
    --stage-dark:#050505;
    --plate-hi:#eceef0;
    --plate-mid:#d3d6da;
    --plate-lo:#b9bdc2;
    --plate-edge:#8c9096;
    --screw-dark:#3a3d41;
    --screw-light:#c9ccd0;
    --lcd-bg:#030603;
    --lcd-frame:#a7abb0;
    --lcd-green:#3fe34e;
    --ink:#1e2124;
    --scale-ink:#2a2c2f;
    --placeholder:#a3a7ad;
    --series-red:#b0141a;
    --photo-a:#4a4f52;
    --photo-b:#8a8478;
  }
  *{margin:0;padding:0;box-sizing:border-box}
  html,body{width:1200px;height:750px;overflow:hidden;background:var(--stage-dark)}
  .banner{
    position:relative;width:1200px;height:750px;overflow:hidden;
    background:radial-gradient(ellipse 70% 60% at 45% 22%,var(--stage-light) 0%,#2c2c2c 55%,var(--stage-dark) 100%);
  }
  .plate{
    position:absolute;left:24px;top:170px;width:1150px;height:406px;
    border:2px solid var(--plate-edge);border-radius:3px;
    background:
      repeating-linear-gradient(90deg,rgba(255,255,255,.10) 0 1px,rgba(0,0,0,.03) 1px 3px),
      linear-gradient(100deg,var(--plate-lo) 0%,var(--plate-hi) 30%,var(--plate-mid) 55%,var(--plate-hi) 75%,var(--plate-lo) 100%);
    box-shadow:inset 0 2px 0 rgba(255,255,255,.7),inset 0 -2px 0 rgba(0,0,0,.25),0 8px 20px rgba(0,0,0,.7);
  }
  .screw{
    position:absolute;width:38px;height:38px;border-radius:50%;
    background:radial-gradient(circle at 40% 35%,var(--screw-light) 0%,#8d9196 45%,var(--screw-dark) 100%);
    box-shadow:inset 0 0 0 3px #5d6065,0 1px 2px rgba(0,0,0,.5);
  }
  .screw::after{
    content:"";position:absolute;left:12px;top:12px;width:14px;height:14px;border-radius:50%;
    background:radial-gradient(circle,#2a2c2f 0%,#55585c 100%);
  }
  .screw.tl{left:34px;top:179px}.screw.tr{left:1127px;top:179px}
  .screw.bl{left:34px;top:527px}.screw.br{left:1127px;top:527px}

  .schedule{
    position:absolute;left:386px;top:194px;width:365px;height:101px;
    background:var(--lcd-bg);border:3px solid var(--lcd-frame);
    box-shadow:inset 0 0 12px rgba(0,0,0,.9);
    font-family:"Share Tech Mono",monospace;color:var(--lcd-green);
    text-shadow:0 0 6px rgba(63,227,78,.6);text-align:center;overflow:hidden;
  }
  .schedule-day{font-size:32px;line-height:1;margin-top:10px;letter-spacing:1px;white-space:nowrap}
  .schedule-times{
    display:flex;flex-wrap:nowrap;justify-content:space-between;
    padding:10px 22px 0;font-size:32px;line-height:1;letter-spacing:1px;white-space:nowrap;
  }
  .schedule-times span{white-space:nowrap}

  .logo-slot{
    position:absolute;left:82px;top:256px;width:273px;height:192px;
    border:1px dotted #8f949a;text-align:center;color:var(--placeholder);
    font-family:"Tinos",serif;line-height:1.12;padding-top:12px;
  }
  .logo-slot .big{font-size:34px;display:block}
  .logo-slot .small{font-size:24px;display:block}

  .power{
    position:absolute;left:110px;top:473px;width:48px;height:48px;border-radius:50%;
    background:radial-gradient(circle at 45% 35%,#ffffff 0%,#d7dadd 55%,#9da1a6 100%);
    box-shadow:0 1px 3px rgba(0,0,0,.45),inset 0 0 0 1px #a8acb1;
  }
  .power svg{position:absolute;left:12px;top:12px}
  .series-name{
    position:absolute;left:91px;top:533px;font-family:"Oswald",sans-serif;font-weight:500;
    font-size:22px;line-height:1;color:var(--series-red);text-transform:uppercase;letter-spacing:.3px;white-space:nowrap;
  }

  .volume{position:absolute;left:442px;top:330px;width:260px;height:260px}
  .volume-cap{
    position:absolute;left:515px;top:403px;width:114px;height:114px;border-radius:50%;
    background:conic-gradient(from 20deg,#f7f5ee,#b9b4a2,#e9e6dc,#8f8a7b,#f2efe6,#aaa594,#e7e3d8,#9d9888,#f7f5ee);
    box-shadow:0 0 0 3px #cfd2d5;
  }
  .volume-pointer{position:absolute;left:442px;top:330px}

  .host-frame{
    position:absolute;left:843px;top:235px;width:234px;height:234px;border-radius:50%;
    background:linear-gradient(150deg,#f4f5f6 0%,#8b8f94 35%,#ffffff 55%,#6f7378 80%,#d9dcdf 100%);
    box-shadow:0 4px 10px rgba(0,0,0,.45);
  }
  .host-photo{
    position:absolute;left:15px;top:15px;width:204px;height:204px;border-radius:50%;
    background:radial-gradient(circle at 50% 40%,var(--photo-b) 0%,var(--photo-a) 70%,#2d3133 100%);
    box-shadow:inset 0 0 0 2px #3b3f43;
  }
  .host-name{
    position:absolute;left:810px;top:489px;width:300px;text-align:center;white-space:nowrap;
    font-family:"Oxanium",sans-serif;font-weight:600;font-size:26px;letter-spacing:3px;color:var(--ink);line-height:1;
  }
</style>
</head>
<body>
<main class="banner">
  <section class="plate" aria-label="Deep Orbit DJ set panel"></section>
  <span class="screw tl"></span><span class="screw tr"></span>
  <span class="screw bl"></span><span class="screw br"></span>

  <div class="schedule">
    <p class="schedule-day">FRIDAY</p>
    <p class="schedule-times"><span>02:00 PM</span><span>08:00 PM</span></p>
  </div>

  <div class="logo-slot">
    <span class="big">Your</span>
    <span class="small">Text,</span>
    <span class="small">Logo,</span>
    <span class="small">Anything</span>
    <span class="big">HERE</span>
  </div>

  <div class="power">
    <svg width="24" height="24" viewBox="0 0 24 24" fill="none" stroke="#3a3d41" stroke-width="2.4" stroke-linecap="round">
      <path d="M7.5 6.5a7 7 0 1 0 9 0"/><line x1="12" y1="3" x2="12" y2="11"/>
    </svg>
  </div>
  <p class="series-name">Deep Orbit</p>

  <svg class="volume" viewBox="0 0 260 260" font-family="Arimo, sans-serif" font-size="15" fill="#2a2c2f" text-anchor="middle" dominant-baseline="middle">
    <circle cx="130" cy="130" r="76" fill="#1d1f22"/>
    <circle cx="130" cy="130" r="76" fill="none" stroke="#dfe1e3" stroke-width="4" stroke-dasharray="1.5 4"/>
    <g stroke="#2a2c2f" stroke-width="2">
      <line x1="92.6" y1="198.5" x2="88.8" y2="205.5"/>
      <line x1="63.2" y1="170.2" x2="56.3" y2="174.3"/>
      <line x1="52" y1="130.8" x2="44" y2="130.9"/>
      <line x1="62.3" y1="91.2" x2="55.4" y2="87.3"/>
      <line x1="91.2" y1="62.3" x2="87.3" y2="55.4"/>
      <line x1="130.8" y1="52" x2="130.9" y2="44"/>
      <line x1="170.2" y1="63.2" x2="174.3" y2="56.3"/>
      <line x1="198.5" y1="92.6" x2="205.5" y2="88.8"/>
      <line x1="208" y1="132.4" x2="216" y2="132.7"/>
      <line x1="196" y1="171.6" x2="202.8" y2="175.8"/>
      <line x1="165.9" y1="199.3" x2="169.6" y2="206.4"/>
    </g>
    <text x="80" y="221">0</text><text x="41" y="184">1</text>
    <text x="26" y="131">2</text><text x="40" y="78">3</text>
    <text x="78" y="40">4</text><text x="131" y="26">5</text>
    <text x="184" y="41">6</text><text x="221" y="80">7</text>
    <text x="234" y="133">8</text><text x="218" y="185">9</text>
    <text x="178" y="222">10</text>
  </svg>
  <div class="volume-cap"></div>
  <svg class="volume-pointer" width="260" height="260" viewBox="0 0 260 260">
    <line x1="113" y1="160" x2="102" y2="180" stroke="#111" stroke-width="5" stroke-linecap="round"/>
  </svg>

  <div class="host-frame">
    <div class="host-photo" role="img" aria-label="Photo of the featured DJ"></div>
  </div>
  <p class="host-name">DJ KALVANNE</p>
</main>
</body>
</html>
```